Bright Fern Series- Face & Body Oil Label

Hi,
I need a label design for a new brand- "Bright Fern Series". Modern and expensive looking. Any color scheme. Feel free to be creative! (I'm not set on the brand name above... I was also thinking maybe "TIRA" or "PuraLume".
-Packaging: 4oz / 118mL clear glass "boston round" bottle with a white treatment pump. The product is an oil so it has a golden tint.
-Product: 4oz Biotin & Marula Face & Body Oil (note that the featured ingredients will change. Others will be "Rosehip & Vitamin E", "Lavender & Hemp Seed Oil", "Coconut Oil & Vitamin C"
-Label size: 5" x 2.5" rounded corners
-Main Highlight: "Moisturizing & Healing"
-Other Highlights:
-----non-greasy
-----all-natural
-----paraben-free
-----vegan
(feel free to use icon symbols)
-Ingredient deck attached
-Other info:
----made in Los Angeles, CA
----manufactured by Willowmere Labs LLC
----UPC
The main thing here is the logo and textures to the label. I can fill in / rearrange the info after.
Thank you,
Owen

```html
<!DOCTYPE html>
<html lang="en">
<head>
<meta charset="utf-8">
<title>PuraLume – Biotin &amp; Marula Face &amp; Body Oil Label</title>
<link rel="stylesheet" href="https://fonts.googleapis.com/css2?family=Libre+Baskerville:wght@400;700&family=Playfair+Display:wght@700&family=Oswald:wght@400&family=Josefin+Sans:wght@400;600&family=Montserrat:wght@400&display=swap">
<style>
  :root {
    --page: #e8e8e9;
    --label-brown: #4a362c;
    --panel-dark: #261a16;
    --bar-dark: #1f1512;
    --gold-light: #f3d46b;
    --gold: #c9a03a;
    --gold-deep: #8a6218;
    --cream: #ffffff;
    --muted: #e9e2da;
  }
  * { box-sizing: border-box; margin: 0; padding: 0; }
  html, body { width: 1200px; height: 1200px; overflow: hidden; background: var(--page); }

  .label {
    position: absolute; left: 250px; top: 50px; width: 700px; height: 1100px;
    background: var(--label-brown); border-radius: 28px; overflow: hidden;
    font-family: "Montserrat", sans-serif; color: var(--cream);
  }

  .title-panel {
    position: absolute; left: 93px; top: 0; width: 510px; height: 492px;
    background: var(--panel-dark);
    border: 2px solid var(--gold-deep); border-top: none;
    border-radius: 0 0 44px 44px;
    text-align: center;
  }
  .brand {
    position: absolute; top: 24px; width: 100%;
    font-family: "Libre Baskerville", serif; font-weight: 400;
    font-size: 60px; line-height: 1; color: var(--cream);
  }
  .brand-rule {
    position: absolute; top: 98px; left: 135px; width: 240px; height: 3px;
    background: linear-gradient(90deg, transparent, var(--gold-light), var(--gold), transparent);
  }
  .series {
    position: absolute; top: 110px; width: 100%;
    font-family: "Josefin Sans", sans-serif; font-size: 21px; color: var(--gold);
    letter-spacing: 0.5px;
  }
  .ingredients {
    position: absolute; top: 152px; width: 100%;
    font-family: "Libre Baskerville", serif; font-weight: 700;
    font-size: 52px; color: var(--cream); white-space: nowrap;
  }
  .product-name {
    position: absolute; top: 228px; left: 0; width: 100%;
    font-family: "Playfair Display", serif; font-weight: 700;
    white-space: nowrap;
  }
  .product-line {
    display: block;
    background: linear-gradient(180deg, var(--gold-light) 0%, var(--gold) 55%, var(--gold-deep) 100%);
    -webkit-background-clip: text; background-clip: text; color: transparent;
  }
  .product-line--face {
    font-size: 112px; line-height: 118px; letter-spacing: -2px;
  }
  .product-line--body {
    font-size: 104px; line-height: 110px; letter-spacing: -3px;
    transform: scaleX(0.84); transform-origin: 50% 50%;
  }

  .ingredient-art {
    position: absolute; left: 110px; top: 505px; width: 480px; height: 270px;
    border-radius: 40%;
    background: radial-gradient(ellipse at 50% 55%, #c9c83e 0%, #9aa534 35%, #6b5a2a 65%, var(--label-brown) 100%);
  }

  .claim-box {
    position: absolute; left: 124px; top: 792px; width: 448px; height: 112px;
    border: 2px solid var(--gold); border-radius: 14px; overflow: hidden; text-align: center;
  }
  .claim-main {
    height: 62px; line-height: 62px;
    background: linear-gradient(90deg, var(--gold-deep), var(--gold), var(--gold-light), var(--gold), var(--gold-deep));
    font-family: "Oswald", sans-serif; font-size: 40px; color: var(--panel-dark);
    letter-spacing: -0.5px; white-space: nowrap;
  }
  .claim-origin {
    height: 48px; line-height: 50px; background: var(--panel-dark);
    font-family: "Josefin Sans", sans-serif; font-size: 25px; font-weight: 600;
    white-space: nowrap;
  }

  .benefits {
    position: absolute; top: 920px; left: 110px; width: 480px;
    display: flex; justify-content: space-between;
  }
  .benefit {
    flex: 1; text-align: center; border-left: 1px solid rgba(233,226,218,.4);
  }
  .benefit:first-child { border-left: none; }
  .benefit svg { width: 56px; height: 56px; display: block; margin: 0 auto 8px; }
  .benefit span { font-size: 16px; color: var(--muted); white-space: nowrap; }

  .size-bar {
    position: absolute; left: 0; bottom: 0; width: 100%; height: 84px;
    background: var(--bar-dark); border-top: 2px solid var(--gold-deep);
    text-align: center; line-height: 84px; font-size: 20px;
  }
</style>
</head>
<body>
  <main class="label">
    <section class="title-panel">
      <div class="brand">PuraLume</div>
      <div class="brand-rule"></div>
      <div class="series">BRIGHT FERN SERIES</div>
      <h2 class="ingredients">Biotin &amp; Marula</h2>
      <h1 class="product-name">
        <span class="product-line product-line--face">FACE &amp;</span>
        <span class="product-line product-line--body">BODY OIL</span>
      </h1>
    </section>

    <div class="ingredient-art" role="img" aria-label="Illustration of marula fruits on a branch with leaves and a splash of golden oil"></div>

    <section class="claim-box">
      <div class="claim-main">MOISTURIZING &amp; HEALING</div>
      <div class="claim-origin">MADE IN LOS ANGELES, CA</div>
    </section>

    <section class="benefits">
      <div class="benefit">
        <svg viewBox="0 0 56 56" fill="none" stroke="#c9a03a" stroke-width="3">
          <circle cx="28" cy="28" r="25"/>
          <path d="M28 14 C22 24 19 28 19 33 a9 9 0 0 0 18 0 C37 28 34 24 28 14Z"/>
          <line x1="14" y1="14" x2="42" y2="42"/>
        </svg>
        <span>Non-greasy</span>
      </div>
      <div class="benefit">
        <svg viewBox="0 0 56 56" fill="none" stroke="#c9a03a" stroke-width="3">
          <circle cx="28" cy="28" r="25"/>
          <path d="M16 40 C16 24 26 16 40 16 C40 30 32 40 16 40Z"/>
          <line x1="16" y1="40" x2="32" y2="24"/>
        </svg>
        <span>All-natural</span>
      </div>
      <div class="benefit">
        <svg viewBox="0 0 56 56" fill="none" stroke="#c9a03a" stroke-width="3">
          <circle cx="28" cy="28" r="25"/>
          <rect x="21" y="18" width="14" height="22" rx="3"/>
          <line x1="14" y1="14" x2="42" y2="42"/>
        </svg>
        <span>Paraben-free</span>
      </div>
      <div class="benefit">
        <svg viewBox="0 0 56 56" fill="none" stroke="#c9a03a" stroke-width="3">
          <circle cx="28" cy="28" r="25"/>
          <path d="M28 40 C18 36 16 26 18 18 C26 20 30 28 28 40Z"/>
          <path d="M28 40 C38 36 40 26 38 18 C30 20 26 28 28 40Z"/>
        </svg>
        <span>Vegan</span>
      </div>
    </section>

    <footer class="size-bar">4oz / 118mL</footer>
  </main>
</body>
</html>
```